Packaging Design Project

Hello Designers,

Our company is a new start up looking to sell rice bagged in 50kg bags and sold to africa. This packaging should show that the product is trust worthy, homely and portray a mother love and trust ie your mother know the best food for her child.

Please find enclosed our company logo enclosed(Dunmore fields) and the name of the rice is bright table. We will add later bright table gold,premium and ultra .

Front Of the bag

Top of the bag is our logo

Name: Bright Table

Picture:to be done by you

Country of origin:Vietnam Parboiled RIce

Description:100% SORTEXED

Quality:premium quality

Back of bag

Name of company:DUNMORE FIELDS

Production Date:

expiry date:

Batch number:

Origination of product:PRODUCT OF VIETNAM

Exported by : name to be provided

Reason: I would like to see more designers. We were also asked for the length and breath of the 50kg bags. length is 92cm and breath is 63cm.

WE HAVE BEEN INFORMED BY THE BAG PRINTERS THAT WE ARE LIMITED TO ONLY 3 COLOURS.PLEASE CAN YOU UPDATE YOUR DESIGNS TO JUST 3 COLORS

Target Market(s)

The target market is all women above the age of 16.

Industry/Entity Type

It Company

Requirements
Must have
• We must have a picture of an african mother preferably smiling, her age must be at least 50 to 60 years of age.

```html
<!DOCTYPE html>
<html lang="en">
<head>
<meta charset="utf-8">
<title>Bright Table – Rice Bag Presentation</title>
<link rel="stylesheet" href="https://fonts.googleapis.com/css2?family=Archivo:wght@800&family=Alfa+Slab+One&family=Yanone+Kaffeesatz:wght@400&family=Roboto+Slab:wght@700&display=swap">
<style>
  :root {
    --navy: #0b2350;
    --backdrop: #01224f;
    --royal: #0a5fb0;
    --sky: #2f8ad6;
    --yellow: #fcd000;
    --gold-light: #fff2bf;
    --gold: #e8c969;
    --rice-light: #f7f7f5;
    --rice-mid: #e2e2de;
    --white: #ffffff;
  }
  * { margin: 0; padding: 0; box-sizing: border-box; }
  html, body {
    width: 1200px; height: 800px; overflow: hidden;
    background: var(--white);
    position: relative;
  }
  .defs { position: absolute; width: 0; height: 0; }
  .presentation-panel {
    position: absolute; left: 572px; top: 0; width: 628px; height: 800px;
    background: var(--backdrop);
  }
  .bag {
    position: absolute; width: 507px; height: 716px; overflow: hidden;
    transform-origin: 0 0;
  }
  .bag--main { left: 633px; top: 41px; }
  .bag--back { left: 112px; top: 150px; transform: scale(0.79); box-shadow: 0 6px 14px rgba(0,0,0,0.18); }
  .bag--front { left: 62px; top: 164px; transform: scale(0.79); box-shadow: 0 6px 14px rgba(0,0,0,0.25); }
  .rice-texture {
    position: absolute; inset: 0;
    background: radial-gradient(ellipse at 50% 45%, var(--rice-light) 0%, var(--rice-mid) 100%);
  }
  .artwork { position: absolute; inset: 0; }
  .brand-band {
    position: absolute; left: 0; right: 0; top: 45px; height: 24px;
    background: var(--yellow);
  }
  .brand-plate {
    position: absolute; left: 67px; top: 0; width: 355px; height: 24px;
    background: var(--white);
    display: flex; align-items: center; justify-content: center; gap: 8px;
  }
  .brand-dot { width: 20px; height: 20px; border-radius: 50%; background: var(--royal); }
  .brand-name {
    font-family: "Archivo", Arial, sans-serif; font-weight: 800;
    font-size: 24px; letter-spacing: 1px; color: var(--navy);
  }
  .quality-badge {
    position: absolute; left: 314px; top: 140px; width: 138px; height: 80px;
    border-radius: 50%;
    background: radial-gradient(ellipse at 40% 35%, var(--gold-light) 0%, var(--gold) 100%);
    display: flex; flex-direction: column; align-items: center; justify-content: center;
    line-height: 1;
  }
  .badge-figure { font-family: "Roboto Slab", Georgia, serif; font-weight: 700; font-size: 30px; color: var(--navy); }
  .badge-label { font-family: "Yanone Kaffeesatz", Arial, sans-serif; font-size: 22px; color: var(--royal); margin-top: 2px; }
  .product-name {
    position: absolute; right: 72px; top: 406px; text-align: right;
    font-family: "Alfa Slab One", Georgia, serif; font-weight: 400;
    font-size: 50px; line-height: 56px; color: var(--royal);
    -webkit-text-stroke: 9px var(--white); paint-order: stroke fill;
  }
  .quality-line {
    position: absolute; left: 187px; top: 560px;
    font-family: "Yanone Kaffeesatz", Arial, sans-serif;
    font-size: 36px; line-height: 40px; color: var(--navy); letter-spacing: 0.5px;
  }
  .origin-band {
    position: absolute; left: 0; right: 0; top: 636px; height: 42px;
    background: var(--yellow);
    display: flex; align-items: center; padding-left: 47px;
  }
  .origin-text { font-family: "Archivo", Arial, sans-serif; font-weight: 800; font-size: 29px; color: var(--navy); }
</style>
</head>
<body>
  <svg class="defs" aria-hidden="true">
    <defs>
      <linearGradient id="photoTone" x1="0" y1="0" x2="1" y2="1">
        <stop offset="0" stop-color="#7a4a34"/>
        <stop offset="0.55" stop-color="#5a3424"/>
        <stop offset="1" stop-color="#3f8a86"/>
      </linearGradient>
      <g id="bagArtwork">
        <path class="swoosh-upper" d="M40,100 C150,80 260,98 335,135 L322,140 C250,108 150,94 40,106 Z" fill="var(--royal)"/>
        <path class="family-photo" d="M0,140 C120,110 250,110 320,140 C375,190 385,330 350,430 C320,500 250,525 0,530 Z" fill="url(#photoTone)"/>
        <path class="crescent-navy" d="M290,128 C400,150 440,260 425,370 C410,470 320,540 0,565 L0,530 C250,525 320,500 350,430 C385,330 375,190 320,140 Z" fill="var(--navy)"/>
        <path class="crescent-sky" d="M420,210 C495,300 495,420 430,490 C375,545 250,565 0,588 L0,575 C260,552 390,510 440,440 C478,370 470,280 420,210 Z" fill="var(--sky)"/>
        <path class="swoosh-lower" d="M0,600 C70,590 130,578 190,562 L186,568 C130,586 70,598 0,607 Z" fill="var(--royal)"/>
      </g>
    </defs>
  </svg>

  <div class="presentation-panel"></div>

  <section class="bag bag--back" aria-label="Rice bag, rear of pair">
    <div class="rice-texture"></div>
    <svg class="artwork" width="507" height="716" viewBox="0 0 507 716" role="img" aria-label="Photo of a smiling African mother with her two daughters"><use href="#bagArtwork"/></svg>
    <div class="brand-band"><div class="brand-plate"><span class="brand-dot"></span><span class="brand-name">DUNMORE FIELDS</span></div></div>
    <div class="quality-badge"><span class="badge-figure">100%</span><span class="badge-label">Sortexed</span></div>
    <p class="product-name">BRIGHT<br>TABLE</p>
    <p class="quality-line">Premium Quality Rice</p>
    <div class="origin-band"><span class="origin-text">Vietnam Parboiled RIce</span></div>
  </section>

  <section class="bag bag--front" aria-label="Rice bag, front of pair">
    <div class="rice-texture"></div>
    <svg class="artwork" width="507" height="716" viewBox="0 0 507 716" role="img" aria-label="Photo of a smiling African mother with her two daughters"><use href="#bagArtwork"/></svg>
    <div class="brand-band"><div class="brand-plate"><span class="brand-dot"></span><span class="brand-name">DUNMORE FIELDS</span></div></div>
    <div class="quality-badge"><span class="badge-figure">100%</span><span class="badge-label">Sortexed</span></div>
    <p class="product-name">BRIGHT<br>TABLE</p>
    <p class="quality-line">Premium Quality Rice</p>
    <div class="origin-band"><span class="origin-text">Vietnam Parboiled RIce</span></div>
  </section>

  <main class="bag bag--main">
    <div class="rice-texture" role="img" aria-label="Background of white parboiled rice grains"></div>
    <svg class="artwork" width="507" height="716" viewBox="0 0 507 716" role="img" aria-label="Photo of a smiling African mother embracing her two daughters"><use href="#bagArtwork"/></svg>
    <div class="brand-band"><div class="brand-plate"><span class="brand-dot"></span><span class="brand-name">DUNMORE FIELDS</span></div></div>
    <div class="quality-badge"><span class="badge-figure">100%</span><span class="badge-label">Sortexed</span></div>
    <h1 class="product-name">BRIGHT<br>TABLE</h1>
    <p class="quality-line">Premium Quality Rice</p>
    <div class="origin-band"><span class="origin-text">Vietnam Parboiled RIce</span></div>
  </main>
</body>
</html>
```